Business Broker Website

This website will be for a business broker. The logo is attached and will need to be in the footer as it is but in the header please remove the word 'group' and replace with 'business sales' (so that it is morvale business sales).
It needs to be a modern high end corporate font for the logo and also for the rest of the site. Please only use fonts available on fonts.google.com
It needs to have 4 prominent boxes at the top of the page that say 'business listings', 'appraisal report', 'what we do' and 'who we are'
The 'what we do' section needs to have sub menu items for 'sectors' and 'services'. The who we are section needs to have sub menu items for 'about us' and 'team'
The top menu needs to have :
* Home
* Businesses for Sale
* Sell your Business
* What we do
* About Us
* Contact
This needs to be seen as the #1 business broker in Australia. It needs to attract serious high quality buyers and sellers and needs to be highly professional, premium and straight to the point and innovative.
It needs to show that Morvale Business Sales not only do SME sales but also do Corporate Mergers and Acquisitions.
They like the look of the site at https://brackenhurstadvisors.com/en-us/
They also love the look of https://quarlingcapital.com/ (they prefer this to the above site)
The website features a clean, minimalist layout with ample white space, making it easy to navigate and visually appealing. The typography is modern and legible, and the color palette is professional, enhancing the site's overall aesthetic. High-quality images and a responsive design contribute to its polished appearance.
Please note this is for an Australian based business.
Contact details to show in the footer:
Head Office
Suite 17, Second Floor
48 Tarrant Street
Oakmere Vale
VIC 3842
1300 62 19 05
info@morvalegroup.com.au
If you need some wording for the site, look at https://www.morvalegroup.com.au/businesssales which is a page about their business division. Don't use all this content though as they want it straight to the point and not rambling on.

```html
<!DOCTYPE html>
<html lang="en">
<head>
<meta charset="utf-8">
<title>Morvale Business Sales</title>
<link rel="stylesheet" href="https://fonts.googleapis.com/css2?family=Poppins:wght@400;500;600;700&family=Caveat:wght@500&display=swap">
<style>
  :root {
    --orange: #f0532f;
    --teal: #2f4b57;
    --teal-light: #3d5c68;
    --card: #f5f2ee;
    --ink: #1b1b1b;
    --muted: #6b6b6b;
    --white: #ffffff;
    --stage: #e4e4e4;
  }
  * { box-sizing: border-box; margin: 0; padding: 0; }
  html, body { width: 1187px; height: 1200px; overflow: hidden; }
  body { background: var(--stage); font-family: "Poppins", sans-serif; color: var(--ink); }

  .page {
    position: absolute; left: 365px; top: 10px;
    width: 577px; height: 1487px;
    background: var(--white);
    transform: scale(0.793); transform-origin: top left;
  }
  .abs { position: absolute; }

  /* Hero */
  .hero-bg { left: 37px; top: 19px; width: 503px; height: 297px; }
  .brand-pill {
    background: var(--white); border-radius: 10px;
    display: flex; align-items: center; gap: 4px; padding: 0 7px;
    font-weight: 600; color: var(--ink);
  }
  .brand-pill .dot { width: 7px; height: 7px; border-radius: 50%; background: var(--orange); }
  .header-brand { left: 52px; top: 32px; width: 60px; height: 19px; font-size: 8px; }
  .main-nav {
    left: 162px; top: 32px; width: 271px; height: 19px;
    background: var(--white); border-radius: 10px;
    display: flex; align-items: center; justify-content: space-around;
    font-size: 5.6px; padding: 0 4px;
  }
  .btn-contact {
    left: 478px; top: 32px; width: 50px; height: 19px;
    background: var(--orange); color: var(--white); border-radius: 10px;
    font-size: 5.8px; display: flex; align-items: center; justify-content: center;
  }
  .hero-kicker { left: 91px; top: 73px; color: var(--white); font-size: 11.5px; font-weight: 500; }
  .hero-title {
    left: 91px; top: 88px; color: var(--white); font-size: 23px; font-weight: 700;
    line-height: 26px; letter-spacing: -0.3px;
  }
  .hero-title .accent { color: var(--orange); }

  /* Search */
  .search-panel {
    left: 54px; top: 236px; width: 276px; height: 116px;
    background: var(--orange); border-radius: 16px;
  }
  .field {
    position: absolute; height: 17px; border: 0.8px solid rgba(255,255,255,0.85);
    border-radius: 9px; color: var(--white); font-size: 4.8px;
    display: flex; align-items: center; padding: 0 6px; justify-content: space-between;
  }
  .field svg { width: 5px; height: 5px; }
  .field.num { justify-content: flex-end; }
  .price-label { left: 26px; top: 66px; color: var(--white); font-size: 4.6px; }
  .search-btn {
    left: 261px; top: 81px; width: 15px; height: 15px; border-radius: 50%;
    background: var(--white); display: flex; align-items: center; justify-content: center;
  }

  /* Feature cards */
  .card {
    position: absolute; width: 247px; height: 128px;
    background: var(--card); border-radius: 12px; overflow: hidden;
  }
  .card::after {
    content: ""; position: absolute; right: 0; bottom: 0;
    width: 34px; height: 24px; background: var(--white); border-top-left-radius: 10px;
  }
  .card h2 { position: absolute; left: 19px; top: 17px; font-size: 15px; font-weight: 600; letter-spacing: -0.2px; }
  .card .icon { position: absolute; left: 200px; top: 19px; width: 30px; height: 28px; }
  .card p { position: absolute; left: 19px; top: 76px; width: 150px; font-size: 4.6px; line-height: 7px; color: var(--muted); }
  .card .go {
    position: absolute; right: 11px; bottom: 4px; z-index: 1;
    width: 15px; height: 15px; border-radius: 50%; background: var(--orange);
    display: flex; align-items: center; justify-content: center;
  }

  /* Experience */
  .team-photo {
    left: 37px; top: 685px; width: 247px; height: 168px; border-radius: 12px;
    background: linear-gradient(135deg, #e9e2d6 0%, #c9b7a0 40%, #3a3f4a 75%, #d9d3cb 100%);
  }
  .exp-script { left: 311px; top: 712px; font-family: "Caveat", cursive; font-size: 19px; color: var(--orange); }
  .exp-title { left: 311px; top: 733px; font-size: 14.5px; font-weight: 600; }
  .exp-copy { left: 311px; top: 769px; width: 220px; font-size: 4.6px; line-height: 7px; color: var(--muted); }
  .exp-copy p + p { margin-top: 6px; }

  /* Appraisal banner */
  .appraisal-bg { left: 37px; top: 893px; width: 503px; height: 136px; }
  .appraisal-title { left: 103px; top: 926px; font-size: 22px; font-weight: 600; color: var(--white); letter-spacing: -0.4px; }
  .appraisal-title .accent { color: var(--orange); }
  .appraisal-copy { left: 104px; top: 964px; width: 150px; font-size: 4.6px; line-height: 7px; color: var(--white); }
  .btn-outline {
    left: 407px; top: 942px; width: 50px; height: 19px;
    border: 0.8px solid var(--white); border-radius: 10px; color: var(--white);
    font-size: 5.8px; display: flex; align-items: center; justify-content: center;
  }

  /* Sell */
  .sell-title { left: 37px; top: 1085px; font-size: 14.5px; font-weight: 600; }
  .sell-title .accent { color: var(--orange); }
  .sell-copy { left: 38px; top: 1121px; width: 228px; font-size: 4.6px; line-height: 7px; color: var(--muted); }
  .sell-copy p + p { margin-top: 6px; }
  .broker-photo {
    left: 292px; top: 1070px; width: 248px; height: 168px; border-radius: 12px;
    background: linear-gradient(120deg, #b4583f 0%, #c26a4e 35%, #2a3340 60%, #a9553d 100%);
  }

  /* Footer */
  .site-footer {
    left: 0; top: 1279px; width: 577px; height: 208px;
    background: linear-gradient(90deg, var(--teal) 0%, var(--teal-light) 100%);
    color: var(--white);
  }
  .footer-brand { left: 45px; top: 46px; width: 60px; height: 20px; font-size: 8px; }
  .footer-col h3 { font-size: 5px; font-weight: 600; margin-bottom: 7px; }
  .footer-col { font-size: 4.8px; line-height: 7px; }
  .office { left: 182px; top: 50px; }
  .office .row { display: flex; gap: 6px; margin-bottom: 6px; }
  .office svg { width: 6px; height: 6px; flex: none; margin-top: 0.5px; }
  .links { left: 336px; top: 50px; }
  .links li { list-style: none; margin-bottom: 5.5px; color: rgba(255,255,255,0.8); }
  .social { left: 431px; top: 50px; }
  .social .icons { display: flex; gap: 7px; }
  .social .icons span { width: 6px; height: 6px; border-radius: 50%; background: var(--white); }
  .copyright { left: 0; width: 577px; top: 176px; text-align: center; font-size: 4.6px; color: rgba(255,255,255,0.8); }
</style>
</head>
<body>
<div class="page">

  <!-- Hero -->
  <svg class="abs hero-bg" viewBox="0 0 503 297" role="img" aria-label="Melbourne city skyline and river bridge at dusk">
    <defs>
      <linearGradient id="heroSky" x1="0" y1="0" x2="0" y2="1">
        <stop offset="0" stop-color="#2c3140"/>
        <stop offset="0.45" stop-color="#4a4f5c"/>
        <stop offset="0.7" stop-color="#6b5547"/>
        <stop offset="1" stop-color="#3a2a24"/>
      </linearGradient>
    </defs>
    <path fill="url(#heroSky)" d="M14,0 H489 Q503,0 503,14 V215 Q503,229 489,229 H473 Q459,229 459,243 V253 Q459,267 445,267 H395 Q381,267 381,281 V283 Q381,297 367,297 H14 Q0,297 0,283 V14 Q0,0 14,0 Z"/>
  </svg>

  <div class="abs brand-pill header-brand"><span class="dot"></span>Morvale</div>
  <nav class="abs main-nav">
    <span>Home</span><span>Businesses for Sale</span><span>Sell your Business</span><span>What we do</span><span>About Us</span>
  </nav>
  <div class="abs btn-contact">Contact</div>

  <div class="abs hero-kicker">Your Partner in Melbourne</div>
  <h1 class="abs hero-title"><span class="accent">Real Estate</span> and<br>Business Sales</h1>

  <form class="abs search-panel">
    <div class="field" style="left:26px;top:18px;width:59px">All Types <svg viewBox="0 0 10 10"><path d="M2 4l3 3 3-3" fill="none" stroke="#fff" stroke-width="1"/></svg></div>
    <div class="field" style="left:95px;top:18px;width:87px">Search Keyword...</div>
    <div class="field" style="left:191px;top:18px;width:86px">All Properties <svg viewBox="0 0 10 10"><path d="M2 4l3 3 3-3" fill="none" stroke="#fff" stroke-width="1"/></svg></div>
    <div class="field" style="left:26px;top:42px;width:121px">All Categories <svg viewBox="0 0 10 10"><path d="M2 4l3 3 3-3" fill="none" stroke="#fff" stroke-width="1"/></svg></div>
    <div class="field" style="left:156px;top:42px;width:121px">All States <svg viewBox="0 0 10 10"><path d="M2 4l3 3 3-3" fill="none" stroke="#fff" stroke-width="1"/></svg></div>
    <div class="abs price-label">Price range: $0 to $1,000,000,000</div>
    <div class="field num" style="left:26px;top:80px;width:107px">0.00</div>
    <div class="field num" style="left:143px;top:80px;width:107px">1,000,000,000.00</div>
    <div class="abs search-btn"><svg width="7" height="7" viewBox="0 0 10 10"><circle cx="4.3" cy="4.3" r="3" fill="none" stroke="#1b1b1b" stroke-width="1"/><path d="M6.5 6.5L9 9" stroke="#1b1b1b" stroke-width="1"/></svg></div>
  </form>

  <!-- Feature cards -->
  <article class="card" style="left:37px;top:385px">
    <h2>Business Listings</h2>
    <svg class="icon" viewBox="0 0 30 28" fill="none" stroke="#1b1b1b" stroke-width="1.3" stroke-linecap="round">
      <path d="M3 5l2 2 3-4M3 14l2 2 3-4M3 23l2 2 3-4"/><path d="M13 6h15M13 15h15M13 24h15"/>
    </svg>
    <p>Selling a business can be a complex and daunting endeavour. At the Morvale Group, we list, market, negotiate, and then sell your business, taking all the stress out of the process for you.</p>
    <span class="go"><svg width="7" height="7" viewBox="0 0 10 10"><path d="M2 5h6M5.5 2.5L8 5 5.5 7.5" fill="none" stroke="#fff" stroke-width="1"/></svg></span>
  </article>
  <article class="card" style="left:292px;top:385px">
    <h2>Appraisal Report</h2>
    <svg class="icon" viewBox="0 0 30 28" fill="none" stroke="#1b1b1b" stroke-width="1.3" stroke-linecap="round">
      <path d="M4 3h17v20a3 3 0 0 0 3 3H9a3 3 0 0 1-3-3V6a3 3 0 0 0-3-3"/><path d="M21 22h6v1a3 3 0 0 1-3 3"/><path d="M10 9h8M10 14h8M10 19h6"/>
    </svg>
    <p>Selling a business can be a complex and daunting endeavour. At the Morvale Group, we list, market, negotiate, and then sell your business, taking all the stress out of the process for you.</p>
    <span class="go"><svg width="7" height="7" viewBox="0 0 10 10"><path d="M2 5h6M5.5 2.5L8 5 5.5 7.5" fill="none" stroke="#fff" stroke-width="1"/></svg></span>
  </article>
  <article class="card" style="left:37px;top:520px">
    <h2>What We Do</h2>
    <svg class="icon" viewBox="0 0 30 28" fill="none" stroke="#1b1b1b" stroke-width="1.3" stroke-linecap="round" stroke-linejoin="round">
      <path d="M1 10l6-4 5 2 5-2 6 1 6 3"/><path d="M4 12l8 8 3 2 3-2 5-5 5-4"/><path d="M12 8l-4 5 3 1 4-3 5 4"/><path d="M10 17l3 3M13 14l3 3"/>
    </svg>
    <p>Selling a business can be a complex and daunting endeavour. At the Morvale Group, we list, market, negotiate, and then sell your business, taking all the stress out of the process for you.</p>
    <span class="go"><svg width="7" height="7" viewBox="0 0 10 10"><path d="M2 5h6M5.5 2.5L8 5 5.5 7.5" fill="none" stroke="#fff" stroke-width="1"/></svg></span>
  </article>
  <article class="card" style="left:292px;top:520px">
    <h2>Who We Are</h2>
    <svg class="icon" viewBox="0 0 30 28" fill="none" stroke="#1b1b1b" stroke-width="1.3" stroke-linecap="round">
      <circle cx="15" cy="9" r="7"/><path d="M2 27c2-7 7-10 13-10s11 3 13 10"/>
    </svg>
    <p>Selling a business can be a complex and daunting endeavour. At the Morvale Group, we list, market, negotiate, and then sell your business, taking all the stress out of the process for you.</p>
    <span class="go"><svg width="7" height="7" viewBox="0 0 10 10"><path d="M2 5h6M5.5 2.5L8 5 5.5 7.5" fill="none" stroke="#fff" stroke-width="1"/></svg></span>
  </article>

  <!-- Experience -->
  <div class="abs team-photo" role="img" aria-label="Three brokers reviewing documents in a bright office"></div>
  <div class="abs exp-script">87 Years' Combined</div>
  <h2 class="abs exp-title">Our Experience</h2>
  <div class="abs exp-copy">
    <p>Our Team of property, business and sales professionals is here for you.</p>
    <p>Whether you are looking for a trusted partner to manage your commercial or industrial property, help you purchase your next family home or find a buyer for your business who is willing to pay the right price – you have come to the right location.</p>
  </div>

  <!-- Appraisal banner -->
  <svg class="abs appraisal-bg" viewBox="0 0 503 136" aria-hidden="true">
    <path fill="var(--teal)" d="M14,0 H489 Q503,0 503,14 V53 Q503,67 489,67 H473 Q459,67 459,81 V91 Q459,105 445,105 H367 Q353,105 353,119 V122 Q353,136 339,136 H14 Q0,136 0,122 V14 Q0,0 14,0 Z"/>
  </svg>
  <h2 class="abs appraisal-title">Book an <span class="accent">Appraisal</span></h2>
  <p class="abs appraisal-copy">Want to know how much your home, commercial property or business is worth? Get in touch with our team today for an obligation-free appraisal.</p>
  <div class="abs btn-outline">Contact</div>

  <!-- Sell your business -->
  <h2 class="abs sell-title">Sell Your <span class="accent">Business</span></h2>
  <div class="abs sell-copy">
    <p>Selling a business can be a complex and daunting endeavour. At the Morvale Group, we list, market, negotiate, and then sell your business, taking all the stress out of the process for you.</p>
    <p>How?</p>
    <p>To facilitate the sale, we leverage a mix of strategies across digital marketing, advertising, trade publications where appropriate, and we maintain and communicate with an up-to-date database of potential buyers.</p>
    <p>We also market specifically to business migrants via ongoing overseas seminars in association with a migration specialist.</p>
  </div>
  <div class="abs broker-photo" role="img" aria-label="Two brokers standing in front of a red brick wall"></div>

  <!-- Footer -->
  <footer class="abs site-footer">
    <div class="abs brand-pill footer-brand"><span class="dot"></span>Morvale</div>
    <div class="abs footer-col office">
      <h3>Head Office</h3>
      <div class="row">
        <svg viewBox="0 0 10 10" fill="none" stroke="#fff" stroke-width="0.8"><rect x="2" y="1" width="6" height="8"/><path d="M4 3h2M4 5h2M4 7h2"/></svg>
        <div>Suite 17, Second Floor<br>48 Tarrant Street<br>Oakmere Vale<br>VIC 3842</div>
      </div>
      <div class="row">
        <svg viewBox="0 0 10 10" fill="none" stroke="#fff" stroke-width="0.8"><path d="M2 1.5l2 .5 1 2-1.2 1a5 5 0 0 0 2.2 2.2l1-1.2 2 1 .5 2C5 9 1 5 2 1.5z"/></svg>
        <div>1300 62 19 05</div>
      </div>
      <div class="row">
        <svg viewBox="0 0 10 10" fill="none" stroke="#fff" stroke-width="0.8"><rect x="1" y="2.5" width="8" height="5.5"/><path d="M1 2.5l4 3 4-3"/></svg>
        <div>info@morvalegroup.com.au</div>
      </div>
    </div>
    <div class="abs footer-col links">
      <h3>Quick Links</h3>
      <ul><li>About</li><li>Disclaimer</li><li>Privacy</li><li>Careers</li><li>Contact</li></ul>
    </div>
    <div class="abs footer-col social">
      <h3>Connect Us</h3>
      <div class="icons"><span></span><span></span><span></span><span></span><span></span></div>
    </div>
    <div class="abs copyright">Copyright © 2025 MORVALE BUSINESS SALES</div>
  </footer>

</div>
</body>
</html>
```